■【予防矯正とは】
予防矯正は発育期のお子様に最小限の器具とワイヤーを用いて(使用しない場合もあります)お口の周りの筋肉や呼吸をアクティビティーという訓練を行うことで正常に整えることで歯並びを正しくする治療法です。

この治療の目的は、悪い歯並びを予防したりきれいにすることだけではありません。
お口や呼吸の正常な発育を目的として、将来にわたって健康な生活を送れるようにお口や呼吸の機能を整えることが一番の目的です。

予防矯正治療の優れた面

1.歯並びがきれいになり見た目がよくなります。
2.噛み合わせがよくなることにより噛む力が向上し、また発音が明瞭になることがあります。
3.歯並びがよくなることで歯磨きがしやすくなり、歯の寿命が長くなる可能性があります。
4.口腔機能の正常な発育が期待できますので食べ物を噛む、飲み込むという摂食嚥下の面において将来にわたって健康な生活が期待できます。
5.正常な呼吸が身につくことで健康面でも病気にかかりにくい、集中力が高まるなどの効果が期待できます。
6.歯並びを作る環境が整うので治療後に歯並びがあとから乱れたりする後戻りが起きる危険性が通常の矯正治療に比べ少ない。
7.ワイヤーや器具が最小限なのでむし歯などになりにくい、歯を磨きやすい、ワイヤーを締めた時の痛みがないなどの面で通常の矯正治療よりも優れています。
8.無理な力が歯にかかりすぎることがないため歯の根が壊れたり、吸収することがありません。
9.将来のお子様が高齢者になった時にいつまでも美味しく口から食事がとれることが期待できます。

雰囲気がよくわかるHPが(当院ではありませんが)以下のリンクにありますのでご確認ください。
http://www.hoshizora-dental.com/original5.html

当院のHPは
http://www.kawasedental.jp/

■【ポスターの目的】
お母さんたちは呼吸や口の筋肉の発達不全で歯並びが悪くなってしまうことをご存じありません。歯並びはもちろんですが病気になりやすかったり、姿勢が悪かったり、集中力がないのも呼吸が悪かったり舌の機能が発達していなかったりすることが原因になっていることがよくあります。
これらを歯科医院の待合室でご覧いただいたときに「えっ?そんなすごい治療があるの?」と思って頂き、行動を起こして頂けることが目的です。
----------
若いお母さん目線で気軽に相談できそうなデザイン頂けると幸いです。
----------
単純に歯並びを悪くさせないという予防というだけでなく、心身ともに健康でいてもらえるための一つの貢献として考えています。

ある方の経験談を頂きました。
こんな子供たちのように後悔をさせたくない・・・お母さん方にも子育てをこうかいさせという思いが強くあります。

歯科には、困ってから来る人が大多数で、予防で困っている人は少ないかもしれません。
予防してこなかったことで痛みを感じている人は、あ、そういえば こんなところにも!と思い出しました。

それは、どんなことかと言いますと、
歯医者での出来事ではなく、他の現場での声です。

私は、長野県に在住で、KAROミュージックの活動で、音楽セラピーや、リハビリなどを、こども病院の院内学級、高齢者施設、病院の精神科、保育、教育現場の領域で25年以上続けています。

活動の中で気になるのは、クライアントさんのご家族や現場スタッフの声に、けっこう「痛み」が入っていることです。
音楽では、その場で今すぐには解決が難しい痛み、なんです。
例えば、高齢者施設の場合、こんな声がよく聞かれます。

「もっと早くに、歯科でみてもらえばよかった。」
「この好物を、自分の歯で、噛ませて味あわせてあげたかった。」
「唾液が少なくて、食事も進辛いけど、音楽セッションで声を出した後は、よく召し上がるんですよ。」
「口の中の予防なんて、こんなに悪くなってから知っても遅いわよ」

そして、小学生、中学生などの場合、

「歯並びの悪さを気にして、歯を出して笑わないんですよ、この子」(セッション中や、集合写真で)
「いつも、頬杖ついたり、足組したりして、歯や姿勢がゆがんでるって、今になっていわれてもねえ。」(発生練習の時に、肩の高さの違いなどから感じたことを共有した時に、反抗期の男児親から。)
「前の学年で口臭が元で、いじめにあって、今も歌も歌わないし、しゃべらないの、あの生徒」(担任の先生)

などなどがあります。

■【ポスターのサイズはA3】
A3サイズでトンボ・塗り足しを入れて作成してください。
縦横はお任せします

■【納品形式】
① ai形式。
② 文字アウトライン化済みファイルと、していないファイルで納品。
③ 写真を使用する場合、高解像度でお願いします。
aiファイルと別に、写真ファイルの納品もお願いします。

【お願い】
頂いたポスター内容を一部変更する可能性があることをご了承ください。
デザインは当社HPにアーカイブとして掲載されることをご了承。
「悪い歯並びは予防できる!」「歯並びを治すと体も健康になる!」
気持ちとしては以下のような気持ちです。

以下、引用します。

大切なあなたとあなたの大切な方に私たちはこう考えます。

寝たきりになって、体が動かなくなって、歩けなくなって、
好きなものを食べられなくなって、転んでしまって・・・
後悔する。そんな後悔を私たちは大好きなあなたにさせたくありません。

あなたの大事なお子様に、歯並びで、食べられないことで、お話がうまくできないこと、口臭で悩むこと・・そんな後悔をさせたくありません。

今は、何も不自由を感じないかもしれません。
だけどこれらの後悔は早く予防すれば消してしまう事ができます。

そのために行動を起こすのはいつでしょうか?
それは”今”です。
あなたは、これからの人生で今より若くなることはありません。
あなたの周りのお子様は今からどんどん成長していきます。
成長の頂点までの距離は今日が一番長いのです。

ですから今すぐ私たちにお手伝いさせてください。

治療内容の説明がとても分かりやすいとスタッフたちにも、来院者のママたちからも好評でした。写真もクシャクシャの笑顔がとてもかわいくみんなの目を引くように思います。何度も修正いただき、有難うございました。

たくさんの皆さんにご提案頂き、本当に有難うございました。
どの方のご提案も本当に素晴らしく、また、私の依頼の文面をしっかりとお読みいただき、様々な角度からご提案頂けましたことを心から感謝申し上げます。
特に何度も修正いただきましたKTStudio様、Borlen様、Hoshino pr様、TERUV2718GK様お手数をおかけしました。最後まで色々と迷いました。本当に素晴らしいご提案を本当に有難うございました。
何卒、今後ともよろしくお願い申し上げます。

```html
<!DOCTYPE html>
<html lang="ja">
<head>
<meta charset="UTF-8">
<title>予防矯正で</title>
<link href="https://fonts.googleapis.com/css2?family=M+PLUS+1p:wght@500;800;900&display=swap" rel="stylesheet">
<style>
  :root {
    --magenta: #e31f7a;
    --pink-text: #e0468c;
    --band: rgba(255, 255, 255, 0.78);
    --bg-light: #fde9f1;
    --bg-mid: #f6bcd3;
    --bg-deep: #ee9bbd;
  }
  html, body {
    margin: 0;
    padding: 0;
    overflow: hidden;
    background: #ffffff;
  }
  .poster {
    position: relative;
    width: 848px;
    height: 1200px;
    overflow: hidden;
    font-family: "M PLUS 1p", sans-serif;
    background: var(--bg-light);
  }
  .poster__photo {
    position: absolute;
    inset: 0;
    background:
      radial-gradient(ellipse 55% 40% at 70% 42%, rgba(255,255,255,0.7), rgba(255,255,255,0) 70%),
      radial-gradient(ellipse 60% 35% at 45% 72%, var(--bg-deep), rgba(238,155,189,0) 75%),
      linear-gradient(180deg, var(--bg-light) 0%, var(--bg-mid) 55%, var(--bg-light) 100%);
  }
  .poster__title {
    position: absolute;
    top: 6px;
    left: 0;
    right: 0;
    margin: 0;
    text-align: center;
    font-size: 132px;
    font-weight: 900;
    line-height: 1;
    letter-spacing: 2px;
    color: var(--magenta);
    text-shadow: 0 0 6px #ffffff, 0 0 2px #ffffff;
  }
  .benefits {
    position: absolute;
    top: 132px;
    left: 20px;
    right: 20px;
    margin: 0;
    font-size: 30.5px;
    font-weight: 500;
    line-height: 53.5px;
    color: var(--pink-text);
    text-align: justify;
    text-align-last: left;
  }
  .benefits__band {
    background: var(--band);
    -webkit-box-decoration-break: clone;
    box-decoration-break: clone;
    padding: 4px 0;
  }
  .benefits__num {
    color: var(--magenta);
    font-weight: 800;
  }
  .benefits__key {
    color: var(--magenta);
    font-weight: 800;
  }
</style>
</head>
<body>
  <div class="poster">
    <div class="poster__photo" role="img" aria-label="笑顔の子どもの写真（淡いピンクのトーン）"></div>
    <h1 class="poster__title">予防矯正で</h1>
    <p class="benefits"><span class="benefits__band"><span class="benefits__num">❶</span>歯並びがきれいになり<span class="benefits__key">見た目がよくなります。</span><span class="benefits__num">❷</span>噛み合わせがよくなることにより<span class="benefits__key">噛む力が向上し</span>、また<span class="benefits__key">発音が明瞭になる</span>ことがあります。<span class="benefits__num">❸</span>歯並びがよくなることで<span class="benefits__key">歯磨きがしやすくなり</span>、<span class="benefits__key">歯の寿命が長くなる</span>可能性があります。<span class="benefits__num">❹</span>口腔機能の正常な発育が期待できますので<span class="benefits__key">食べ物を噛む、飲み込む</span>という摂食嚥下の面において将来にわたって<span class="benefits__key">健康な生活</span>が期待できます。<span class="benefits__num">❺</span>正常な呼吸が身につくことで<span class="benefits__key">健康面でも病気にかかりにくい、集中力が高まる</span>などの効果が期待できます。<span class="benefits__num">❻</span>歯並びを作る環境が整うので治療後に歯並びがあとから乱れたりする<span class="benefits__key">後戻りが起きる危険性</span>が通常の矯正治療に比べ少ない。<span class="benefits__num">❼</span>ワイヤーや器具が最小限なので<span class="benefits__key">むし歯などになりにくい、歯を磨きやすい</span>、ワイヤーを締めた時の<span class="benefits__key">痛みがない</span>などの面で通常の矯正治療よりも優れています。<span class="benefits__num">❽</span>無理な力が歯にかかりすぎることがないため<span class="benefits__key">歯の根が壊れたり、吸収することがありません。</span><span class="benefits__num">❾</span>将来のお子様が高齢者になった時にいつまでも<span class="benefits__key">美味しく口から食事がとれる</span>ことが期待できます。</span></p>
  </div>
</body>
</html>
```